Bref créative
Healthcare apparel brand
Business Card, Letter head, Envelope, Email stationary
I need double sided standard sized Business Card [3.5" x 2"]
Bank Gothic and complimenting fonts
Professional
Marcus Pellandrou
CEO / Founder
482 Folwell Lane Suite B217
Santa Barbara, CA 93184
marcusp@brightloomwovens.example
www.veltunic.example
the corporation is Bright Loom Wovens LLC. The brand is Vel Tunic. I want to prominently display the green cross. Large. Maybe watermark. slogan "Fabrics for Change"
"A highly technical base layer which permanently guards against degradation from micro-organisms." and either one of
"A better choice" or "Just what the doctor ordered"
Logo

```html
<!DOCTYPE html>
<html lang="en">
<head>
<meta charset="utf-8">
<title>VelTunic Stationery</title>
<link href="https://fonts.googleapis.com/css2?family=Michroma&family=Open+Sans:wght@400;600&display=swap" rel="stylesheet">
<style>
  :root {
    --bg: #1c1d1e;
    --paper: #ffffff;
    --green: #8cc63f;
    --ink: #2b2b2b;
    --muted: #8a8a8a;
    --faint: #eef5e4;
    --black-card: #111111;
  }
  * { margin: 0; padding: 0; box-sizing: border-box; }
  html, body { width: 1200px; height: 281px; overflow: hidden; background: var(--bg); }
  .board { position: relative; width: 1200px; height: 281px; font-family: "Open Sans", sans-serif; color: var(--ink); }
  .brand { font-family: "Michroma", sans-serif; letter-spacing: .08em; text-transform: uppercase; }
  .mark-square { display: inline-block; background: var(--green); }

  .brand-lockup { position: absolute; left: 60px; top: 10px; width: 110px; text-align: center; color: var(--paper); }
  .brand-lockup .mark-square { width: 30px; height: 30px; }
  .brand-lockup .brand { font-size: 8px; margin-top: 6px; }
  .brand-lockup .slogan { font-size: 5px; color: var(--muted); letter-spacing: .2em; margin-top: 3px; text-transform: uppercase; }

  .card { position: absolute; width: 100px; height: 57px; background: var(--paper); }
  .card-front { left: 64px; top: 74px; padding: 7px; }
  .card-front .logo { display: flex; align-items: center; gap: 3px; }
  .card-front .mark-square { width: 7px; height: 7px; }
  .card-front .brand { font-size: 5px; }
  .card-front .person { font-size: 3.4px; margin-top: 7px; line-height: 1.5; color: var(--ink); }
  .card-front .person b { font-weight: 600; }

  .card-back { top: 166px; display: flex; flex-direction: column; align-items: center; justify-content: center; gap: 4px; }
  .card-back .mark-square { width: 13px; height: 13px; }
  .card-back .brand { font-size: 5px; }
  .card-back.white { left: 12px; }
  .card-back.green { left: 120px; background: var(--green); }
  .card-back.green .mark-square { background: var(--black-card); }
  .card-back.green .brand { color: var(--black-card); }
  .card-back.black { left: 228px; background: var(--black-card); color: var(--paper); }

  .letterhead { position: absolute; top: 14px; width: 190px; height: 250px; background: var(--paper); padding: 14px 14px; overflow: hidden; }
  .letterhead.first { left: 350px; }
  .letterhead.second { left: 555px; }
  .letterhead .logo { display: flex; align-items: center; gap: 4px; }
  .letterhead .mark-square { width: 8px; height: 8px; }
  .letterhead .brand { font-size: 6px; }
  .letterhead .tagline { font-size: 3.5px; color: var(--muted); margin-top: 3px; }
  .letterhead .contact { position: absolute; right: 14px; top: 12px; font-size: 3.4px; line-height: 1.5; color: var(--muted); text-align: left; }
  .letterhead .watermark { position: absolute; left: 50%; top: 56%; transform: translate(-50%, -50%); display: flex; flex-direction: column; align-items: center; gap: 8px; }
  .letterhead .watermark .mark-square { width: 70px; height: 70px; background: var(--faint); }
  .letterhead .watermark .brand { font-size: 11px; color: var(--faint); }
  .letterhead .footer { position: absolute; left: 14px; right: 14px; bottom: 10px; font-size: 3.2px; color: var(--muted); border-top: 0.5px solid var(--green); padding-top: 3px; }

  .slip { position: absolute; left: 762px; width: 150px; background: var(--paper); padding: 8px; }
  .slip.top { top: 40px; height: 68px; }
  .slip.bottom { top: 210px; height: 48px; }
  .slip .logo { display: flex; align-items: center; gap: 3px; }
  .slip .mark-square { width: 7px; height: 7px; }
  .slip .brand { font-size: 5px; }
  .slip .lines { font-size: 3.3px; color: var(--muted); margin-top: 5px; line-height: 1.5; }

  .envelopes { position: absolute; left: 930px; top: 90px; }
</style>
</head>
<body>
<main class="board">
  <section class="brand-lockup">
    <span class="mark-square"></span>
    <div class="brand">VelTunic</div>
    <div class="slogan">Fabrics for Change</div>
  </section>

  <article class="card card-front">
    <div class="logo"><span class="mark-square"></span><span class="brand">VelTunic</span></div>
    <div class="person">
      <b>Marcus Pellandrou</b><br>CEO / Founder<br>
      482 Folwell Lane Suite B217<br>Santa Barbara, CA 93184<br>
      marcusp@brightloomwovens.example<br>www.veltunic.example
    </div>
  </article>

  <article class="card card-back white"><span class="mark-square"></span><span class="brand">VelTunic</span></article>
  <article class="card card-back green"><span class="mark-square"></span><span class="brand">VelTunic</span></article>
  <article class="card card-back black"><span class="mark-square"></span><span class="brand">VelTunic</span></article>

  <article class="letterhead first">
    <div class="logo"><span class="mark-square"></span><span class="brand">VelTunic</span></div>
    <div class="tagline">Fabrics for Change</div>
    <div class="contact">482 Folwell Lane Suite B217<br>Santa Barbara, CA 93184<br>(805) 555-0142<br>www.veltunic.example</div>
    <div class="watermark"><span class="mark-square"></span><span class="brand">VelTunic</span></div>
    <div class="footer">Bright Loom Wovens LLC · www.veltunic.example</div>
  </article>

  <article class="letterhead second">
    <div class="watermark"><span class="mark-square"></span><span class="brand">VelTunic</span></div>
    <div class="footer">Bright Loom Wovens LLC · www.veltunic.example</div>
  </article>

  <article class="slip top">
    <div class="logo"><span class="mark-square"></span><span class="brand">VelTunic</span></div>
    <div class="lines">A better choice.<br>Fabrics for Change.</div>
  </article>
  <article class="slip bottom">
    <div class="logo"><span class="mark-square"></span><span class="brand">VelTunic</span></div>
    <div class="lines">482 Folwell Lane Suite B217, Santa Barbara, CA 93184</div>
  </article>

  <svg class="envelopes" width="260" height="180" viewBox="0 0 260 180" aria-label="Envelopes">
    <rect x="20" y="0" width="230" height="100" fill="var(--paper)"/>
    <polygon points="20,0 250,0 135,45" fill="var(--green)"/>
    <rect x="10" y="40" width="230" height="100" fill="var(--paper)" stroke="#dcdcdc" stroke-width="0.5"/>
    <polygon points="10,40 240,40 125,85" fill="var(--black-card)"/>
    <rect x="0" y="80" width="230" height="100" fill="var(--paper)" stroke="#dcdcdc" stroke-width="0.5"/>
    <polyline points="0,80 115,125 230,80" fill="none" stroke="#cfcfcf" stroke-width="0.8"/>
    <rect x="12" y="150" width="6" height="6" fill="var(--green)"/>
    <text x="22" y="155.5" font-family="Michroma, sans-serif" font-size="5" fill="var(--ink)" letter-spacing=".4">VELTUNIC</text>
  </svg>
</main>
</body>
</html>
```